Yard sign for Chimney Buisness

I am looking for a 18 Tall x 24" wide yard sign design incorporating our logo/name. We want the signs to stand out and be readable from a distance. only want our logo/business name and website on the sign . www.tallowmerevt.com

Target Market(s)

homeowners

Requirements
Must have
• logo/buisness name
• website
• must be visable at a distance and readable

```html
<!DOCTYPE html>
<html lang="en">
<head>
<meta charset="utf-8">
<title>Tallowmere Sweeps Yard Sign</title>
<link rel="stylesheet" href="https://fonts.googleapis.com/css2?family=Cinzel:wght@400;500;600&family=Cormorant+Garamond:wght@600&display=swap">
<style>
  :root {
    --sign-red: #a30000;
    --sign-white: #ffffff;
    --mark-black: #000000;
    --backdrop: #e9ebee;
  }
  * { margin: 0; padding: 0; box-sizing: border-box; }
  html, body {
    width: 1200px;
    height: 1000px;
    overflow: hidden;
    background: var(--backdrop);
  }
  .yard-sign {
    position: absolute;
    left: 110px;
    top: 132px;
    width: 980px;
    height: 736px;
    background: var(--sign-red);
    overflow: hidden;
  }
  .top-band {
    position: absolute;
    left: 0; top: 0;
    width: 100%;
    height: 256px;
    background: var(--sign-white);
  }
  .brand-mark {
    position: absolute;
    left: 0; top: 88px;
    width: 100%;
    display: flex;
    flex-direction: column;
    align-items: center;
    gap: 28px;
  }
  .brand-mark__square {
    width: 200px;
    height: 200px;
    background: var(--mark-black);
  }
  .brand-mark__name {
    font-family: "Cinzel", serif;
    font-weight: 500;
    font-size: 40px;
    letter-spacing: 6px;
    color: var(--sign-white);
    line-height: 1;
  }
  .business-name {
    position: absolute;
    left: 0; top: 448px;
    width: 100%;
    text-align: center;
    font-family: "Cinzel", serif;
    font-weight: 500;
    font-size: 62px;
    letter-spacing: 3px;
    color: var(--sign-white);
    line-height: 1;
  }
  .established {
    position: absolute;
    left: 126px; top: 518px;
    width: 730px;
    display: flex;
    align-items: center;
    gap: 16px;
  }
  .established__rule {
    flex: 1;
    height: 6px;
    background: var(--sign-white);
  }
  .established__text {
    font-family: "Cinzel", serif;
    font-weight: 400;
    font-size: 40px;
    letter-spacing: 6px;
    color: var(--sign-white);
    line-height: 1;
  }
  .website {
    position: absolute;
    left: 0; top: 618px;
    width: 100%;
    text-align: center;
    font-family: "Cormorant Garamond", serif;
    font-weight: 600;
    font-size: 42px;
    letter-spacing: 4px;
    color: var(--sign-white);
    line-height: 1;
  }
</style>
</head>
<body>
  <main class="yard-sign">
    <div class="top-band"></div>
    <div class="brand-mark">
      <div class="brand-mark__square"></div>
      <div class="brand-mark__name">TALLOWMERE</div>
    </div>
    <h1 class="business-name">TALLOWMERE SWEEPS</h1>
    <div class="established">
      <span class="established__rule"></span>
      <span class="established__text">INC 1989</span>
      <span class="established__rule"></span>
    </div>
    <p class="website">www·tallowmerevt·com</p>
  </main>
</body>
</html>
```